Lone Drift Film - A Caustic Hidden Voyage

Lone Drift is a female-driven psychedelic adventure film about spiritual self-discovery. It's Delia Marchfield’s Brambles on acid--a darkly funny, deeply intimate moment unfolding in altered time.

Uploads/Included Materials:
~Key Artwork (some may need color correction, or higher res / more background images available upon request)
~Draft Lone Drift Poster (and early vision boards)
~Inspo Posters from other films with aesthetics we like
~For the tone/style/feel of the film, please view our early trailer at https://clipnest.example/tarakovel/lonedrifttrailer

In Lone Drift, Henrietta hijacks her ex-boyfriend's acid and hauls out into the wild--alone--to prove she only needs to count on herself. But strangers, Mother Nature, and her own mind have other plans for her, including some phantoms she'll need to embrace.

Lone Drift is gently gritty, playfully intellectual, and, at times, strangely sexy. It blends soft-core thrill, French existential dialogue, and cinéma vérité storytelling into an experimental tapestry. There's a strong ensemble cast, unique original score, stunning visuals of nature, and surprising FX. Thematically, the film tackles "Toxic Independence" -- how mixed messages about self-love and self-importance have left us with the absurd determination to do life alone.

What We Need
A poster that packs a punch while conveying these complex elements as cleanly and beautifully as possible. We want to push past the line of "artsy microbudget film" into "professionally budgeted movie for sale."

1) We're looking for *some* photorealism in a key image (part of Henrietta's face or nature) somewhere in the art, but probably not a standard, fully recognizable front-facing face as the central image.

2) Our Draft Poster (attached) has many positive qualities that could be worth re-exploring: the eyes in the red skies, the smaller image of the character meditating in nature, and even the spork doubling as a spaceship and the colorful/graphic-looking acid (drugs) taking center stage work well. However, we need a clearer and more professional look overall and we are not committed to this design. We'd like the artist to feel free to go in a totally different direction where they see the most potential.

3) We will request all file types / the PSD in the turnaround of this design, and **want the artist to consider how Festival Laurels will eventually fit into the design.**

4) The current tagline is "A Toxically Independent Journey", but we want to also explore "A Caustic Hidden Voyage" or "One Hell of an Inner Journey" (especially if the red skyscape is used).

Target Market(s)

females 18+ (self-discovery, trauma, empowerment), males 35+ (intellectual/adventure/psychedellics)

Industry/Entity Type

Entertainment, adventure, self-growth, female empowerment, nature, dark comedy

Requirements
Must have
• A jaw-dropping central image plus some absurd or thought-provoking
Nice to have
• Eyes in the skies or similar; use of landscape; graphics similar to the red acid, spork, drugs or absurd allusions to the universe, heaven v. hell, or tripping; a sense of danger or tranquility or both juxtaposed
Should not have
• anything too traditionally monotheistic (we lean more hippie/secular inquiry)

```html
<!DOCTYPE html>
<html lang="en">
<head>
<meta charset="utf-8">
<title>Lone Drift – Poster</title>
<link href="https://fonts.googleapis.com/css2?family=Special+Elite&family=Oswald:wght@400;500&family=Anton&display=swap" rel="stylesheet">
<style>
  :root{
    --page:#d9d6d1;
    --ink:#f4f1ec;
    --ink-dim:#d8d2cc;
    --night:#0d0a0c;
    --dusk:#3b2632;
    --plum:#5a3a48;
    --ember:#e2572c;
    --flare:#f4853b;
    --ridge:#1a1114;
  }
  *{margin:0;padding:0;box-sizing:border-box}
  html,body{width:1200px;height:943px;overflow:hidden;background:var(--page)}
  .poster{position:absolute;left:265px;top:0;width:670px;height:943px;background:var(--night);overflow:hidden;color:var(--ink)}
  .key-art{position:absolute;inset:0;
    background:
      radial-gradient(ellipse 70% 9% at 55% 40%, rgba(244,133,59,.85), rgba(226,87,44,.5) 50%, transparent 100%),
      linear-gradient(180deg,
        #4a2a34 0%, var(--dusk) 12%, var(--plum) 22%, #3a2a2c 30%,
        #4a2e2a 36%, #a8432a 40%, var(--ember) 43%, var(--flare) 45%, #c84a2c 48%,
        #6a2a24 50%, var(--ridge) 53%, #140d10 70%, var(--night) 100%);}
  .cast-top{position:absolute;top:34px;left:0;right:0;display:flex;justify-content:space-around;padding:0 22px;
    font-family:"Special Elite",monospace;font-size:12px;letter-spacing:.32em;color:var(--ink-dim)}
  .title{position:absolute;top:470px;left:0;right:0;text-align:center;
    font-family:"Anton",sans-serif;font-size:118px;line-height:1;letter-spacing:.14em;color:#fffaf0;
    text-shadow:0 0 8px rgba(255,255,255,.8),0 0 22px rgba(255,240,220,.55),0 0 40px rgba(255,200,160,.3);
    transform:scaleY(1.2) skewY(-2deg);opacity:.9}
  .tagline{position:absolute;top:654px;left:0;right:0;text-align:center;
    font-family:"Special Elite",monospace;font-size:14px;letter-spacing:.55em}
  .presents{position:absolute;top:699px;left:0;right:0;text-align:center;
    font-family:"Oswald",sans-serif;font-size:15px;letter-spacing:.01em;transform:scaleX(.9)}
  .film-name{position:absolute;top:745px;left:0;right:0;text-align:center;
    font-family:"Special Elite",monospace;font-size:21px;letter-spacing:.3em}
  .billing{position:absolute;left:0;right:0;display:flex;justify-content:center;align-items:center;
    font-family:"Oswald",sans-serif;font-size:14.5px;text-transform:uppercase}
  .billing-cast{top:794px;gap:15px;transform:scaleX(.92)}
  .billing-crew{top:832px;gap:14px;transform:scaleX(.92)}
  .billing-assoc{top:879px;gap:22px;transform:scaleX(.92)}
  .credit{display:flex;align-items:center;gap:4px}
  .credit-role{font-family:"Special Elite",monospace;font-size:5.5px;line-height:1.3;text-align:right;letter-spacing:.08em;color:var(--ink-dim)}
  .credit-name{line-height:.95}
  .credit-join{font-family:"Special Elite",monospace;font-size:5.5px;margin:0 3px;color:var(--ink-dim)}
  .footer-band{position:absolute;left:0;right:0;bottom:0;height:75px;background:rgba(20,16,18,.6)}
</style>
</head>
<body>
<main class="poster">
  <div class="key-art" role="img" aria-label="Photograph of a red and orange sunset sky over dark hills, with a woman seated meditating in the grass below"></div>
  <div class="footer-band"></div>

  <header class="cast-top">
    <span>OWEN FARRADY</span><span>TARA KOVEL</span><span>LENA OSAKI</span>
  </header>

  <h1 class="title">LONE DRIFT</h1>

  <p class="tagline">ONE HELL OF AN INNER JOURNEY</p>
  <p class="presents">LANTERN REEL PICTURES PRESENTS A TARA KOVEL JAUNT</p>
  <p class="film-name">"LONE DRIFT"</p>

  <div class="billing billing-cast">
    <span>Tara Kovel</span><span>Owen Farrady</span><span>Lena Osaki</span><span>Pete Moravec</span><span>Dan Ellery</span><span>Ray Quintero</span>
  </div>

  <div class="billing billing-crew">
    <div class="credit"><span class="credit-role">DIRECTED<br>BY</span><span class="credit-name">TARA<br>KOVEL</span></div>
    <div class="credit"><span class="credit-role">DIRECTOR OF<br>PHOTOGRAPHY</span><span class="credit-name">NORA WELLS<br>TAMSIN</span></div>
    <div class="credit"><span class="credit-role">EXECUTIVE<br>PRODUCER</span><span class="credit-name">TARA<br>KOVEL</span></div>
    <div class="credit"><span class="credit-role">PRODUCED<br>BY</span><span class="credit-name">HUGH<br>BRANDISH</span><span class="credit-join">AND</span><span class="credit-name">TARA<br>KOVEL</span></div>
  </div>

  <div class="billing billing-assoc">
    <div class="credit"><span class="credit-role">ASSOCIATE<br>PRODUCERS</span><span class="credit-name">MIRA CASTELLO</span></div>
    <span>COLIN VERHOEVEN</span><span>ADA LINWOOD</span><span>FELIX DORN</span>
  </div>
</main>
</body>
</html>
```